Revamp Of Landing Page For an Automated AI Voice Agents Agency

here is my current landing page https://app.brightfunnelstudio.example/v2/preview/KXWQPmR4hLsDnTfYvJcA?notrack=true

Please use all my current content and imagery of ai agents in your new design. Make it easy to ready, easy to navigate and easy to understand

I am looking for a SLEEK shiny polished looking website. I like Dark themed sites but am open to see light themed sites too so please dont be shy.

The site should have an Ai Voice Agent Theme about it. Maybe look and feel of futureistic but simple and not intimidating to the average person...

Here are a couple website designs I like for reference:
https://q4t.example/
https://ai-bots.mervinholt.example/
https://chatvexo.example/ai-agents

Target Market(s)

b2b

Industry/Entity Type

AI Voice Agents

Coding

Coded - Design and coding required

Font styles to use
Other font styles liked:
• open

Requirements
Must have
• all elements and content and images used in existing design.
Nice to have
• open
Should not have
• open

```html
<!DOCTYPE html>
<html lang="en">
<head>
<meta charset="utf-8">
<title>Voxaline — AI Voice Agents</title>
<link href="https://fonts.googleapis.com/css2?family=Poppins:wght@300;400;500;600;700&display=swap" rel="stylesheet">
<style>
:root{
  --bg:#060509;
  --panel:#111016;
  --panel-2:#1a1920;
  --line:rgba(255,255,255,.16);
  --text:#ffffff;
  --muted:#b9b7c4;
  --purple:#6a3ff0;
  --purple-deep:#3a1d9c;
  --violet:#8d5cff;
  --accent:#5a38e8;
  --light:#e6e6ea;
  --ink:#15141a;
  --orange:#f7a23b;
  --green:#2fbf8f;
}
*{box-sizing:border-box;margin:0;padding:0}
html,body{width:1200px;height:5259px;overflow:hidden;background:var(--bg)}
body{font-family:'Poppins',sans-serif;color:var(--text);position:relative}
.abs{position:absolute}
.btn{display:inline-block;border-radius:999px;font-size:14px;padding:9px 18px;border:1px solid var(--line);background:#2a2930;color:#fff}
.glow{position:absolute;border-radius:50%;filter:blur(60px);pointer-events:none}

/* hero */
.hero{position:absolute;left:0;top:0;width:1200px;height:675px;overflow:hidden}
.hero-art{position:absolute;left:0;top:0;width:620px;height:675px;background:
  radial-gradient(ellipse 260px 90px at 280px 230px,rgba(90,210,200,.55),transparent 70%),
  radial-gradient(ellipse 300px 120px at 170px 120px,rgba(120,80,230,.55),transparent 70%),
  radial-gradient(ellipse 320px 140px at 380px 310px,rgba(60,70,160,.5),transparent 70%),
  #07060b}
.nav{position:absolute;top:45px;left:62px;right:62px;height:36px;display:flex;align-items:center}
.brand{display:flex;align-items:center;gap:10px;font-size:26px;font-weight:500;letter-spacing:2px;color:#fff}
.brand .dot{width:22px;height:22px;border:2px solid #fff;border-radius:50%}
.nav-links{position:absolute;left:528px;display:flex;gap:26px;font-size:14px}
.nav-cta{position:absolute;right:0;background:#fff;color:var(--accent);border-radius:999px;padding:6px 14px;font-size:14px;font-weight:500}
.hero-rule{position:absolute;left:62px;top:322px;width:410px;height:1px;background:rgba(255,255,255,.5)}
.hero h1{position:absolute;left:62px;top:345px;font-size:39px;line-height:50px;font-weight:500;width:460px}
.hero p{position:absolute;left:62px;top:462px;width:435px;font-size:14px;line-height:22px}
.hero .btn{position:absolute;left:62px;top:593px}

.dash{position:absolute;left:567px;top:170px;width:633px;height:505px;background:#fff;border-radius:22px 0 0 22px;overflow:hidden;color:var(--ink)}
.dash-side{position:absolute;left:0;top:0;width:130px;height:100%;background:linear-gradient(180deg,#5b3ff2,#4a2fd8)}
.dash-side .logo{position:absolute;left:18px;top:36px;display:flex;gap:8px;align-items:center;color:#fff;font-size:10px;line-height:12px}
.dash-side .logo span{width:28px;height:28px;background:#fff;border-radius:8px}
.dash-side ul{position:absolute;left:18px;top:110px;list-style:none;font-size:8px;color:rgba(255,255,255,.8)}
.dash-side li{margin-bottom:30px}
.dash-side .promo{position:absolute;left:16px;top:350px;width:98px;height:70px;border-radius:8px;background:rgba(255,255,255,.15)}
.dash-card{position:absolute;border-radius:8px;background:#f5f4fb;font-size:8px;color:#333;padding:6px}
.bars{position:absolute;display:flex;align-items:flex-end;gap:10px}
.bars i{display:block;width:9px;border-radius:5px}

/* workforce */
.section-title{position:absolute;left:0;width:1200px;text-align:center;font-size:38px;font-weight:500;line-height:50px}
.card{position:absolute;border-radius:14px;border:1px solid var(--line);background:linear-gradient(180deg,#1b1a21,#0b0a0f);overflow:hidden;text-align:center}
.card h3{font-size:27px;font-weight:400;line-height:36px;margin-top:38px}
.card p{font-size:14px;line-height:22px;margin:18px auto 0;width:290px}
.card.purple{background:linear-gradient(180deg,#3a21a8,#5a32d6 60%,#4d2bc4)}
.panel{position:absolute;background:#fff;color:var(--ink);text-align:left;border-radius:8px 8px 0 0;overflow:hidden}
.panel .t{font-size:11px;font-weight:500}
.panel .s{font-size:8px;color:#aaa}

.mid-cta{position:absolute;left:200px;width:800px;top:1847px;text-align:center;font-size:14px;line-height:22px}
.mid-cta .btn{margin-top:16px}

/* install */
.install{position:absolute;left:59px;top:2068px;width:1084px;height:371px;border-radius:30px;overflow:hidden;background:linear-gradient(90deg,#101330,#1b1446 45%,#261458)}
.install-art{position:absolute;left:0;top:0;width:100%;height:100%;background:
  radial-gradient(ellipse 300px 120px at 420px 250px,rgba(120,80,255,.55),transparent 70%),
  radial-gradient(ellipse 260px 90px at 800px 60px,rgba(70,200,210,.4),transparent 70%),
  radial-gradient(ellipse 200px 100px at 600px 170px,rgba(180,110,255,.35),transparent 70%)}
.install h2{position:absolute;left:0;width:100%;top:30px;text-align:center;font-size:38px;font-weight:500}
.install .rule{position:absolute;left:32px;right:32px;top:92px;height:1px;background:var(--line)}
.install .wish{position:absolute;left:60px;top:150px;font-size:40px;line-height:50px;font-weight:500}
.install h4{position:absolute;left:532px;top:150px;width:500px;font-size:22px;line-height:32px;font-weight:500}
.install p{position:absolute;left:532px;top:245px;width:500px;font-size:15px;line-height:22px}

/* never sick */
.sick{position:absolute;top:2621px;height:408px;border-radius:12px;border:1px solid var(--line);background:#000;overflow:hidden;text-align:center}
.sick h3{font-size:27px;font-weight:500}
.sick p{font-size:14px;line-height:20px;position:relative;z-index:1}
.sick .art{position:absolute;left:0;width:100%}

/* ready */
.ready{position:absolute;left:59px;top:3125px;width:1084px;height:525px;border-radius:30px;overflow:hidden;background:linear-gradient(135deg,#1f3138 0%,#2a2c52 50%,#4a2e9a 100%)}
.ready h2{position:absolute;top:45px;width:100%;text-align:center;font-size:38px;font-weight:500}
.ready .bolt{position:absolute;left:410px;top:115px;width:240px;height:380px;background:radial-gradient(ellipse 90px 170px at 50% 50%,rgba(255,220,255,.75),rgba(190,140,255,.35) 60%,transparent 80%)}
.ready .left{position:absolute;left:44px;top:148px;width:400px;font-size:28px;line-height:41px;font-weight:500}
.ready .right{position:absolute;left:603px;top:130px;width:440px;font-size:15px;line-height:23px}
.ready .right .btn{position:absolute;left:205px;top:150px}
.ready .rule{position:absolute;left:44px;right:44px;top:350px;height:1px;background:rgba(255,255,255,.3)}
.ready h3{position:absolute;left:44px;top:405px;font-size:38px;font-weight:500}
.promise{position:absolute;top:475px;font-size:15px;display:flex;align-items:center;gap:10px}

/* testimonial */
.testi{position:absolute;left:67px;top:3745px;width:1068px;height:398px;border-radius:30px;background:var(--light);color:var(--ink)}
.testi h2{position:absolute;left:47px;top:38px;font-size:40px;font-weight:500}
.testi .more{position:absolute;right:50px;top:42px;background:var(--ink);color:#fff;border-radius:999px;padding:9px 18px;font-size:14px;font-weight:500}
.quote{position:absolute;top:110px;width:290px}
.quote p{font-size:15px;line-height:22px;margin-top:20px;color:#333}
.author{display:flex;align-items:center;gap:14px;margin-top:34px;font-size:15px}
.author span.av{width:62px;height:62px;border-radius:50%;background:radial-gradient(circle at 50% 35%,#6a6670,#1d1b22 70%)}

/* faq */
.faq-title{position:absolute;left:66px;top:4320px;font-size:40px;line-height:50px;font-weight:500}
.faq-lead{position:absolute;left:66px;top:4490px;width:330px;font-size:14px;line-height:22px}
.faq-item{position:absolute;left:537px;width:604px;height:55px;border-radius:8px;background:#1b1a21;border:1px solid var(--line);font-size:12px;display:flex;align-items:center;padding:0 30px;justify-content:space-between}
.faq-item b{font-weight:300;font-size:26px}
.faq-open{position:absolute;left:537px;top:4245px;width:604px;height:123px;border-radius:8px;background:#1b1a21;border:1px solid var(--line);font-size:12px;padding:20px 20px;line-height:20px}

/* footer */
.foot-col{position:absolute;top:4795px;font-size:13px;line-height:25px}
.foot-col h5{color:var(--violet);font-size:14px;font-weight:500;margin-bottom:8px;display:flex;gap:8px;align-items:center}
.foot-rule{position:absolute;left:66px;width:1066px;height:1px;background:var(--line)}
.links{position:absolute;top:4962px;font-size:13px;line-height:30px}
.links h5{color:var(--violet);font-size:14px;font-weight:500}
.input{position:absolute;left:722px;top:4992px;width:268px;height:42px;border-radius:999px;background:#1f1e25;border:1px solid var(--line);font-size:12px;color:var(--muted);display:flex;align-items:center;padding-left:36px}
.submit{position:absolute;left:1006px;top:4992px;width:116px;height:42px;border-radius:999px;background:#fff;color:var(--accent);font-weight:500;font-size:15px;display:flex;align-items:center;justify-content:center}
.social{position:absolute;left:722px;top:5094px;display:flex;gap:18px}
.social span{width:20px;height:20px;border-radius:50%;background:#fff}
.legal{position:absolute;top:5222px;font-size:11px}
</style>
</head>
<body>

<section class="hero">
  <div class="hero-art" role="img" aria-label="Abstract glowing iridescent ribbon in teal and purple"></div>
  <nav class="nav">
    <div class="brand"><span class="dot"></span>VOXALINE</div>
    <div class="nav-links"><span>Product</span><span>Example</span><span>Pricing</span><span>About us</span><span>Blog</span></div>
    <div class="nav-cta">Contact us</div>
  </nav>
  <div class="hero-rule"></div>
  <h1>Transforming the Future with AI.</h1>
  <p>We Will Create An AI Agent Customized For Your Business At No Cost. Simply Click The Button Above And Your Very Own Ai Agent Will Be Calling You In Just A Couple Minutes. Experience The Magic And Get Ready To Be Very Impressed!</p>
  <span class="btn">Get An Instant Free Demo</span>

  <div class="dash">
    <div class="dash-side">
      <div class="logo"><span></span>Dashboard<br>Admin</div>
      <ul><li>Home</li><li>Agreements</li><li>Layout</li><li>Documents</li><li>Logout</li></ul>
      <div class="promo"></div>
    </div>
    <div class="dash-card" style="left:150px;top:18px;width:140px;height:82px;background:linear-gradient(135deg,#6a4cf5,#4a2fd8);color:#fff">4821 0093 7715 6032</div>
    <div class="abs" style="left:150px;top:120px;font-size:9px">Card Management</div>
    <div class="dash-card" style="left:150px;top:145px;width:64px;height:70px;background:#e7f8ee">Send Money</div>
    <div class="dash-card" style="left:222px;top:145px;width:64px;height:70px;background:#eaf2ff">Receive Money</div>
    <div class="dash-card" style="left:150px;top:225px;width:64px;height:70px;background:#fff7e6">Send Invoice</div>
    <div class="dash-card" style="left:222px;top:225px;width:64px;height:70px;background:#f3ecff">More Features</div>
    <div class="dash-card" style="left:150px;top:320px;width:136px;height:60px">Product Transaction</div>
    <div class="dash-card" style="left:150px;top:390px;width:136px;height:60px">New Transaction</div>
    <div class="abs" style="left:310px;top:18px;font-size:9px">Company Revenue</div>
    <div class="bars" style="left:318px;top:50px;height:110px"><i style="height:40px;background:#b9a8ff"></i><i style="height:70px;background:#f7a23b"></i><i style="height:55px;background:#6a3ff0"></i><i style="height:90px;background:#f07fd0"></i><i style="height:60px;background:#6a3ff0"></i><i style="height:80px;background:#f7a23b"></i><i style="height:45px;background:#b9a8ff"></i></div>
    <div class="dash-card" style="left:530px;top:18px;width:100px;height:160px"></div>
    <div class="abs" style="left:310px;top:205px;font-size:8px">Cost Monitoring</div>
    <svg class="abs" style="left:310px;top:225px" width="50" height="50" viewBox="0 0 50 50"><circle cx="25" cy="25" r="19" fill="none" stroke="#eee" stroke-width="6"/><circle cx="25" cy="25" r="19" fill="none" stroke="#f7a23b" stroke-width="6" stroke-dasharray="95 120" transform="rotate(-90 25 25)"/></svg>
    <div class="abs" style="left:375px;top:240px;font-size:10px;font-weight:600">$ 8,210.00</div>
    <div class="abs" style="left:310px;top:290px;width:120px;font-size:7px;line-height:14px;color:#555">Business 224<br>Travel 2452<br>Design 476<br>Finance 1021<br>Development 976</div>
    <div class="abs" style="left:460px;top:205px;font-size:8px">Visitors Monitoring</div>
    <svg class="abs" style="left:455px;top:225px" width="170" height="120" viewBox="0 0 170 120"><path d="M0 90 C30 40 50 40 70 70 S120 110 170 30" fill="none" stroke="#6a3ff0" stroke-width="2"/><path d="M0 100 C40 80 80 60 110 85 S150 90 170 70" fill="none" stroke="#f7a23b" stroke-width="2"/></svg>
    <div class="abs" style="left:310px;top:385px;font-size:8px">Payment History</div>
    <div class="abs" style="left:310px;top:405px;width:315px;height:1px;background:#eee"></div>
    <div class="abs" style="left:310px;top:425px;width:315px;font-size:7px;line-height:22px;color:#666">Sale Payment · Paid<br>Credit Card · Paid<br>Bank Transfer · Pending</div>
  </div>
</section>

<div class="glow" style="left:980px;top:660px;width:260px;height:180px;background:rgba(110,60,240,.45)"></div>

<h2 class="section-title" style="top:772px">Meet Your New AI- Powered<br>Workforce</h2>

<div class="card" style="left:53px;top:933px;width:343px;height:410px">
  <h3>Ai Sales Agent</h3>
  <p style="width:300px">Reed will take your inbound sales calls. Will give all detailed information to the customer, answer questions in a normal conversational.</p>
  <div class="panel" style="left:100px;top:195px;width:243px;height:215px;padding:12px">
    <div class="t">Company Revenue</div>
    <div class="bars" style="left:28px;top:45px;height:140px;gap:12px"><i style="height:60px;background:#b9a8ff"></i><i style="height:120px;background:#6a3ff0"></i><i style="height:80px;background:#f7a23b"></i><i style="height:100px;background:#f07fd0"></i><i style="height:70px;background:#6a3ff0"></i><i style="height:110px;background:#f7a23b"></i><i style="height:50px;background:#b9a8ff"></i></div>
  </div>
</div>

<div class="card purple" style="left:429px;top:933px;width:714px;height:410px">
  <h3>Ai Receptionist</h3>
  <p style="width:560px">Milo handles all your calls 24/7. You can also set him to only take overflow calls and after hours. He can send emails and sms messages and even book appointments over the call</p>
  <div class="panel" style="left:55px;top:165px;width:594px;height:245px;padding:24px 34px">
    <div style="font-size:18px">Visitors Monitoring</div>
    <div class="s" style="font-size:12px;margin-top:10px;color:#c2b6ff">Weekly visitors overview</div>
    <div class="abs" style="left:345px;top:28px;display:flex;gap:10px;font-size:10px"><span style="padding:6px 14px;border-radius:6px;background:#f4f4f6;color:#ccc">Monthly</span><span style="padding:6px 14px;border-radius:6px;box-shadow:0 2px 8px rgba(0,0,0,.1)">Weekly</span><span style="padding:6px 14px;border-radius:6px;background:#f4f4f6;color:#ccc">Day</span></div>
    <div style="display:flex;gap:40px;font-size:12px;margin-top:42px;color:#555"><span><i style="display:inline-block;width:9px;height:9px;background:var(--green);margin-right:8px"></i>Check In &nbsp; <b style="font-weight:400;color:#222">245 Visitors</b></span><span><i style="display:inline-block;width:9px;height:9px;background:var(--orange);margin-right:8px"></i>Check Out &nbsp; <b style="font-weight:400;color:#222">245 Visitors</b></span></div>
    <div class="abs" style="left:34px;top:190px;font-size:14px;color:#999">200</div>
    <svg class="abs" style="left:0;top:160px" width="594" height="90" viewBox="0 0 594 90"><path d="M330 90 C380 90 400 20 430 20 S480 90 530 90" fill="none" stroke="#6a3ff0" stroke-width="2"/></svg>
    <div class="abs" style="left:135px;top:198px;width:70px;height:40px;border-radius:8px;background:#3c3c48;color:#fff;font-size:12px;text-align:center;line-height:16px;padding-top:4px">124<br><span style="font-size:8px">New Visitors</span></div>
  </div>
</div>

<div class="card" style="left:53px;top:1376px;width:343px;height:410px">
  <h3 style="margin-top:24px">Ai Appointment<br>Setter</h3>
  <p>Finn offers business advice, helps brainstorm ideas, and provides insights on growth tactics to support your entrepreneurial journey.</p>
  <div class="panel" style="left:40px;top:218px;width:263px;height:192px;background:transparent">
    <div class="abs" style="left:0;top:0;width:124px;height:150px;border-radius:8px;background:#e8f8ee;padding:16px;font-size:13px;color:#222"><i style="display:block;width:20px;height:16px;background:#3ccf82;border-radius:3px;margin-bottom:20px"></i>Send Money<div style="font-size:9px;color:#8a8;margin-top:40px">38 transactions</div></div>
    <div class="abs" style="left:139px;top:0;width:124px;height:150px;border-radius:8px;background:#eaf2ff;padding:16px;font-size:13px;color:#222"><i style="display:block;width:14px;height:14px;border-right:3px solid #3a7af0;border-top:3px solid #3a7af0;margin-bottom:22px"></i>Receive<br>Money<div style="font-size:9px;color:#89a;margin-top:24px">Send link</div></div>
    <div class="abs" style="left:0;top:162px;width:124px;height:40px;border-radius:8px 8px 0 0;background:#fff5e4"></div>
    <div class="abs" style="left:139px;top:162px;width:124px;height:40px;border-radius:8px 8px 0 0;background:#f3ecff"></div>
  </div>
</div>

<div class="card" style="left:429px;top:1376px;width:343px;height:410px">
  <h3 style="margin-top:24px">Ai Lead Qualifier</h3>
  <p style="font-size:13px;line-height:21px">Conversate With Prospects To Qualify Before Handing Over To Sales Team<br><br>All of our ai agents gather information and qualify leads. If they are interested in the services</p>
  <div class="panel" style="left:40px;top:210px;width:263px;height:200px;padding:10px 12px">
    <div class="t">Visitors Monitoring</div>
    <div class="s">Weekly visitors overview</div>
    <svg class="abs" style="left:10px;top:55px" width="243" height="130" viewBox="0 0 243 130"><g stroke="#f0f0f0"><line x1="0" y1="20" x2="243" y2="20"/><line x1="0" y1="55" x2="243" y2="55"/><line x1="0" y1="90" x2="243" y2="90"/></g><path d="M0 100 C40 40 60 30 85 60 S140 110 170 70 S210 30 243 60" fill="none" stroke="#8d5cff" stroke-width="2"/><path d="M0 110 C50 95 90 80 130 105 S200 100 243 90" fill="none" stroke="#f7a23b" stroke-width="2"/><rect x="60" y="22" width="30" height="18" rx="4" fill="#3c3c48"/><rect x="125" y="88" width="30" height="18" rx="4" fill="#3c3c48"/></svg>
  </div>
</div>

<div class="card" style="left:804px;top:1376px;width:343px;height:410px">
  <h3 style="margin-top:24px">Ai Appointment<br>Setter</h3>
  <p>Finn offers business advice, helps brainstorm ideas, and provides insights on growth tactics to support your entrepreneurial journey.</p>
  <div class="panel" style="left:40px;top:210px;width:263px;height:200px;padding:14px 16px">
    <div class="t">Cost Monitoring</div>
    <div class="s">Monthly cost overview</div>
    <svg class="abs" style="left:16px;top:60px" width="70" height="70" viewBox="0 0 70 70"><circle cx="35" cy="35" r="27" fill="none" stroke="#eee" stroke-width="7"/><circle cx="35" cy="35" r="27" fill="none" stroke="#f7a23b" stroke-width="7" stroke-dasharray="136 170" transform="rotate(-90 35 35)"/><text x="35" y="40" text-anchor="middle" font-size="13" font-family="Poppins,sans-serif" fill="#222">80%</text></svg>
    <div class="abs" style="left:100px;top:72px;font-size:8px;color:#8d5cff">Total Income</div>
    <div class="abs" style="left:100px;top:84px;font-size:15px">$ 8,210.00</div>
    <div class="abs" style="left:100px;top:106px;font-size:8px;color:var(--green)">▲ 3.96 %</div>
    <div class="abs" style="left:16px;top:150px;width:230px;font-size:9px;line-height:24px">Business<span style="position:absolute;left:110px">224</span><br>Travel<span style="position:absolute;left:110px">2452</span></div>
  </div>
</div>

<div class="mid-cta">We Will Create An Ai Agent Customized For Your Business At No Cost. Simply Click The Button Above And Your Very Own Ai Agent Will Be Calling You In Just A Couple Minutes. Experience The Magic And Get Ready To Be Very Impressed!<br><span class="btn">Get An Instant Free Demo</span></div>

<div class="glow" style="left:820px;top:1990px;width:360px;height:220px;background:rgba(110,60,240,.4)"></div>
<section class="install">
  <div class="install-art" role="img" aria-label="Abstract flowing glass ribbon in violet and cyan"></div>
  <h2>Install the power of Al for your business</h2>
  <div class="rule"></div>
  <div class="wish">your wish Is<br>their<br>command</div>
  <h4>Your New Ai Agents Will Never Call In Sick And Will Never Complain!</h4>
  <p>With your new team of AI Agents, handling inbound calls, sending emails and sms messages, booking appointments and handling customer service inquiries is going to save you a ton of time and money.</p>
</section>

<h2 class="section-title" style="top:2536px">That Never Gets Sick!</h2>

<div class="sick" style="left:57px;width:343px;border-color:#6a4bd8">
  <h3 style="margin-top:20px">Trained In Seconds</h3>
  <svg style="margin-top:12px" width="64" height="58" viewBox="0 0 64 58" fill="none" stroke="#fff" stroke-width="2.5" stroke-linejoin="round"><path d="M8 20 L22 10 L32 18 L42 10 L56 20 L44 34 L32 46 L20 34 Z"/><path d="M22 30 L30 38 M28 26 L36 34 M34 22 L40 28"/></svg>
  <p style="margin-top:12px">Learns Your Entire Website<br>In Seconds</p>
  <div class="art" role="img" aria-label="Glowing purple wave mesh landscape" style="top:205px;height:203px;background:radial-gradient(ellipse 190px 130px at 50% 75%,#8a6bff,#5230c8 55%,#2a1470 80%,#000)"></div>
</div>
<div class="sick" style="left:431px;width:345px">
  <div class="art" role="img" aria-label="Monochrome wireframe sphere with flowing lines" style="top:0;height:240px;background:radial-gradient(circle at 50% 40%,#bdbdbd,#4a4a4a 45%,#0a0a0a 75%)"></div>
  <h3 style="position:absolute;top:250px;width:100%">Worldwide</h3>
  <svg style="position:absolute;left:148px;top:296px" width="50" height="50" viewBox="0 0 50 50" fill="none" stroke="#fff" stroke-width="2.5"><circle cx="25" cy="25" r="20"/><ellipse cx="25" cy="25" rx="9" ry="20"/><line x1="5" y1="25" x2="45" y2="25"/></svg>
  <p style="position:absolute;top:370px;width:100%">Works Anywhere In The Globe</p>
</div>
<div class="sick" style="left:806px;width:345px">
  <h3 style="margin-top:24px">User-friendly</h3>
  <svg style="margin-top:10px" width="56" height="60" viewBox="0 0 56 60" fill="none" stroke="#fff" stroke-width="2.5"><circle cx="28" cy="34" r="22"/><circle cx="28" cy="34" r="16"/><line x1="28" y1="34" x2="28" y2="24"/><line x1="28" y1="34" x2="35" y2="38"/><rect x="22" y="4" width="12" height="6"/></svg>
  <p style="margin-top:10px">Your Ai Agents Sound As If They're Real<br>Humans</p>
  <div class="art" role="img" aria-label="Monochrome wireframe wave landscape" style="top:250px;height:158px;background:radial-gradient(ellipse 170px 90px at 55% 70%,#9a9a9a,#3a3a3a 55%,#000 85%)"></div>
</div>

<div class="glow" style="left:-40px;top:2980px;width:260px;height:220px;background:rgba(110,60,240,.4)"></div>
<section class="ready">
  <h2>Our Ai Agents Our Ready To Be Hired</h2>
  <div class="bolt" role="img" aria-label="Glowing translucent lightning bolt"></div>
  <div class="left">Lightning-Fast Responses<br>Instant answers, no coffee, bathroom or lunch breaks needed</div>
  <div class="right">We Will Create An Ai Agent Customized For Your Business At No Cost. Simply Click The Button Above And Your Very Own Ai Agent Will Be Calling You In Just A Couple Minutes. Experience The Magic And Get Ready To Be Very Impressed!<span class="btn" style="background:rgba(255,255,255,.12)">Get An Instant Free Demo</span></div>
  <div class="rule"></div>
  <h3>Our Promise To You</h3>
  <div class="promise" style="left:44px"><svg width="28" height="28" viewBox="0 0 28 28" fill="none" stroke="#fff" stroke-width="2"><path d="M14 3 L24 7 V14 C24 20 19 24 14 26 C9 24 4 20 4 14 V7 Z"/><path d="M9 14 L13 18 L19 10"/></svg>14-day money-back guarantee</div>
  <div class="promise" style="left:475px"><svg width="28" height="28" viewBox="0 0 28 28" fill="none" stroke="#fff" stroke-width="2"><path d="M5 16 V13 A9 9 0 0 1 23 13 V16"/><rect x="3" y="15" width="5" height="8" rx="2"/><rect x="20" y="15" width="5" height="8" rx="2"/></svg>24/7 Customer Support</div>
</section>

<section class="testi">
  <h2>Testimonial</h2>
  <span class="more">View More</span>
  <div class="quote" style="left:47px">
    <svg width="52" height="34" viewBox="0 0 52 34" fill="#2b2f7a"><path d="M2 34 L10 4 H22 L14 34 Z M28 34 L36 4 H48 L40 34 Z"/></svg>
    <p>Fames metus cras vestibulum torquent blandit in ultrices fermentum urna per quisque egestas feugiat conubia posuere aliquam molestie montes tristiqueFames</p>
    <div class="author"><span class="av" role="img" aria-label="Client portrait"></span>Owen Hale, New York</div>
  </div>
  <div class="quote" style="left:380px">
    <svg width="52" height="34" viewBox="0 0 52 34" fill="#2b2f7a"><path d="M2 34 L10 4 H22 L14 34 Z M28 34 L36 4 H48 L40 34 Z"/></svg>
    <p>Fames metus cras vestibulum torquent blandit in ultrices fermentum urna per quisque egestas feugiat conubia posuere aliquam molestie montes tristiqueFames</p>
    <div class="author"><span class="av" role="img" aria-label="Client portrait"></span>Liam Brooks, New York</div>
  </div>
  <div class="quote" style="left:757px">
    <svg width="52" height="34" viewBox="0 0 52 34" fill="#2b2f7a"><path d="M2 34 L10 4 H22 L14 34 Z M28 34 L36 4 H48 L40 34 Z"/></svg>
    <p>Fames metus cras vestibulum torquent blandit in ultrices fermentum urna per quisque egestas feugiat conubia posuere aliquam molestie montes tristiqueFames</p>
    <div class="author"><span class="av" role="img" aria-label="Client portrait"></span>Noah Pierce, New York</div>
  </div>
</section>

<div class="glow" style="left:-60px;top:4300px;width:380px;height:300px;background:rgba(90,50,220,.35)"></div>
<div class="glow" style="left:640px;top:4400px;width:420px;height:300px;background:rgba(110,60,240,.3)"></div>
<h2 class="faq-title">Frequently<br>Asked<br>Questions</h2>
<p class="faq-lead">welcome To Our FQA Section, We Address Common Queries About Voxaline Care To Help You Make Informed descion</p>
<span class="btn" style="position:absolute;left:66px;top:4578px;background:#1b1a21">Learn More</span>

<div class="faq-open">What exactly are the AI Voice Agents?<br>AI Voice Agents are specialized human sounding bots, having smart and masterful conversations and each is expertly trained in seconds for a specific business function.<span style="position:absolute;right:20px;top:14px;font-size:20px">×</span></div>
<div class="faq-item" style="top:4378px">How will these AI Voice Agents benefit<b>+</b></div>
<div class="faq-item" style="top:4445px">Are they easy to use?<b>+</b></div>
<div class="faq-item" style="top:4512px">Text Messages, Follow Up Reminders<b>+</b></div>
<div class="faq-item" style="top:4579px">We create your AI Voice Agent and launch it within days!<b>+</b></div>
<div class="faq-item" style="top:4645px">masterful conversations and each is expertly trained in seconds?<b>+</b></div>

<footer>
  <div class="brand abs" style="left:66px;top:4822px"><span class="dot"></span>VOXALINE</div>
  <div class="foot-col" style="left:410px"><h5><svg width="14" height="16" viewBox="0 0 14 16" fill="none" stroke="#8d5cff" stroke-width="1.6"><path d="M7 15 C3 10 1 8 1 6 A6 6 0 0 1 13 6 C13 8 11 10 7 15Z"/><circle cx="7" cy="6" r="2"/></svg>Our location</h5>2870 Larkspur Bend Road<br>Halden Point, IL<br>60417.</div>
  <div class="foot-col" style="left:680px"><h5><svg width="16" height="12" viewBox="0 0 16 12" fill="none" stroke="#8d5cff" stroke-width="1.6"><rect x="1" y="1" width="14" height="10"/><path d="M1 1 L8 7 L15 1"/></svg>Email address</h5>2870 Larkspur Bend Road<br>Halden Point, IL<br>60417.</div>
  <div class="foot-col" style="left:950px"><h5><svg width="14" height="14" viewBox="0 0 14 14" fill="none" stroke="#8d5cff" stroke-width="1.6"><path d="M2 1 L5 1 L6 4 L4 5 C5 7 7 9 9 10 L10 8 L13 9 L13 12 C7 13 1 7 2 1Z"/></svg>Contact number</h5>+124 555 0142<br>+99 548 0177</div>
  <div class="foot-rule" style="top:4935px"></div>
  <div class="links" style="left:66px"><h5>Information</h5>Home<br>About us<br>Terms Of Condition<br>Privacy policy<br>Shop<br>Contact us</div>
  <div class="links" style="left:383px"><h5>Useful links</h5>Privacy Policy<br>Terms Of Condition<br>Gallery<br>Blog</div>
  <div class="links" style="left:727px"><h5>CONTACT US</h5></div>
  <div class="input"><svg style="position:absolute;left:14px" width="14" height="10" viewBox="0 0 14 10" fill="none" stroke="#b9b7c4" stroke-width="1.4"><rect x="1" y="1" width="12" height="8"/><path d="M1 1 L7 5 L13 1"/></svg>Enter Your Email</div>
  <div class="submit">Submit</div>
  <div class="abs" style="left:722px;top:5066px;color:var(--violet);font-size:14px;font-weight:500">FOLLOW US ON</div>
  <div class="social"><span></span><span></span><span></span><span></span><span></span></div>
  <div class="foot-rule" style="top:5200px"></div>
  <div class="legal" style="left:66px">All Rights Reserved © 2025 Voxaline</div>
  <div class="legal" style="left:914px">Privacy Policy</div>
  <div class="legal" style="left:1024px">Terms &amp; Condition</div>
</footer>

</body>
</html>
```